Ridgeway Cafe' eLiquid Label - retro, trendy design

Need a 1.5"x3" label designed for an eLiquid bottle. I like the distressed retro diner look. Feel free to take creative license on logo, images etc. Attaching a mockup I did just to give you an idea of what look I want - the attached concept has all textual elements required....want retro trendy....glenmarsh-ish look and personality...warm colors...high contrasts. attached Vola image is the mockup I want redesigned.

Target Market(s)

eclectic

Industry/Entity Type

Cafe

Font styles to use
Serif
Decorative

Requirements
Must have
• text elements from uploaded sample - 1.5x3 inch high res
Nice to have
• incorporate KD logo somewhere in the design - attached

```html
<!DOCTYPE html>
<html lang="en">
<head>
<meta charset="utf-8">
<title>Ridgeway Café – Volamisu eLiquid Label</title>
<link href="https://fonts.googleapis.com/css2?family=IM+Fell+Double+Pica+SC&family=Rye&family=Cinzel:wght@500&family=Oswald:wght@500&family=Tinos:wght@700&display=swap" rel="stylesheet">
<style>
  :root {
    --page: #f4f4f4;
    --paper-light: #f0cf72;
    --paper-mid: #dca446;
    --paper-edge: #a8621f;
    --ink: #3f2a17;
    --ink-dark: #1e140b;
    --cream: #f3e3c0;
    --teal: #3f8a73;
    --teal-dark: #2e6b58;
    --rust: #9a4d1f;
    --cake: #c98a4a;
  }
  * { box-sizing: border-box; margin: 0; padding: 0; }
  html, body {
    width: 1200px; height: 849px; overflow: hidden;
    background: var(--page);
  }
  .label {
    position: absolute; left: 48px; top: 138px;
    width: 1077px; height: 538px; overflow: hidden;
    background:
      radial-gradient(ellipse 60% 70% at 55% 40%, var(--paper-light) 0%, var(--paper-mid) 55%, var(--paper-edge) 100%);
  }
  .skyline {
    position: absolute; left: 0; right: 0; bottom: 0; height: 360px;
    background: radial-gradient(ellipse 55% 90% at 50% 100%, rgba(90, 55, 20, 0.55) 0%, rgba(110, 70, 25, 0.3) 55%, rgba(120, 80, 30, 0) 100%);
  }
  .web-address {
    position: absolute; left: 20px; top: 24px; height: 490px; width: 48px;
    writing-mode: vertical-rl; transform: rotate(180deg);
    font-family: "Tinos", serif; font-weight: 700; font-size: 38px;
    color: var(--ink-dark); text-align: center; line-height: 48px;
    white-space: nowrap;
  }
  .brand-mark {
    position: absolute; left: 127px; top: 23px;
    width: 124px; height: 124px; border-radius: 50%;
    background: var(--ink);
    display: flex; align-items: center; justify-content: center;
    font-family: "IM Fell Double Pica SC", serif; font-size: 54px; color: var(--paper-mid);
  }
  .brand-name {
    position: absolute; left: 156px; top: 8px; width: 760px;
    font-family: "IM Fell Double Pica SC", serif; font-weight: 400; font-size: 125px;
    color: var(--ink); line-height: 1; text-align: center; white-space: nowrap;
    transform: scaleX(0.72); transform-origin: center;
  }
  .cafe-banner {
    position: absolute; left: 428px; top: 124px; width: 214px; height: 56px;
    background: var(--ink);
    font-family: "Cinzel", serif; font-weight: 500; font-size: 40px;
    color: var(--cream); text-align: center; line-height: 58px; letter-spacing: 2px;
  }
  .flavor-badge { position: absolute; left: 375px; top: 190px; width: 380px; height: 280px; }
  .flavor-art {
    position: absolute; left: 400px; top: 285px; width: 330px; height: 140px;
    border-radius: 40px;
    background: radial-gradient(ellipse at 50% 45%, var(--cake) 0%, #d9b27c 55%, rgba(243, 227, 192, 0.85) 100%);
  }
  .flavor-title {
    position: absolute; left: 375px; top: 218px; width: 380px; text-align: center;
    font-family: "Rye", serif; font-size: 50px; color: var(--rust);
    -webkit-text-stroke: 2px var(--cream); paint-order: stroke fill;
    transform: rotate(3deg); white-space: nowrap;
  }
  .made-in {
    position: absolute; left: 400px; top: 485px; width: 300px; text-align: center;
    font-family: "Tinos", serif; font-weight: 700; font-size: 15px; color: var(--ink-dark);
  }
  .side-column {
    position: absolute; top: 22px; height: 492px;
    writing-mode: vertical-rl; transform: rotate(180deg);
    color: var(--ink-dark);
  }
  .ratio { left: 900px; width: 36px; font-family: "Tinos", serif; font-weight: 700; font-size: 28px; line-height: 36px; white-space: nowrap; }
  .ratio small { font-size: 11px; }
  .ingredients { left: 940px; width: 24px; font-family: "Tinos", serif; font-weight: 700; font-size: 15.5px; line-height: 24px; white-space: nowrap; }
  .warning { left: 972px; width: 60px; font-family: "Oswald", sans-serif; font-weight: 500; font-size: 11px; line-height: 19px; letter-spacing: 0.2px; }
</style>
</head>
<body>
  <main class="label">
    <div class="skyline" role="img" aria-label="Faded distressed city skyline silhouette"></div>

    <p class="web-address">www.ridgewayvapor.com</p>

    <div class="brand-mark">KD</div>
    <h1 class="brand-name">RIDGEWAY</h1>
    <div class="cafe-banner">CAFÉ</div>

    <svg class="flavor-badge" viewBox="0 0 380 280" aria-hidden="true">
      <ellipse cx="190" cy="140" rx="186" ry="136" fill="var(--teal)" stroke="var(--teal-dark)" stroke-width="4"/>
    </svg>
    <div class="flavor-art" role="img" aria-label="Illustration of a layered tiramisu slice on a plate"></div>
    <h2 class="flavor-title">VOLAMISU</h2>

    <p class="made-in">Made in the U.S.A.</p>

    <p class="side-column ratio">70/30 <small>VG</small></p>
    <p class="side-column ingredients">Vegetable Glycerin, Propylene Glycol, Flavoring, Nicotine</p>
    <p class="side-column warning">PROP 65: KEEP OUT OF REACH FROM CHILDREN AND PETS. NPCC POISON HOTLINE: 800-555-0199. NICOTINE IS A CHEMICAL KNOWN IN THE STATE OF CALIFORNIA TO CAUSE BIRTH DEFECTS AND OTHER REPRODUCTIVE HARM. NICOTINE IS AN ADDICTIVE CHEMICAL DERIVED FROM TOBACCO. 18+ ONLY.</p>
  </main>
</body>
</html>
```